Cloud-based vaccination website

Basic website design for cloud-based medical company

Coding

Coded - Design and coding required

Number of Pages Required

1 page

Colors
3277b5

```html
<!DOCTYPE html>
<html lang="en">
<head>
<meta charset="utf-8">
<title>NUBRIX – Modern Digital Software Solutions</title>
<link href="https://fonts.googleapis.com/css2?family=Raleway:wght@500;600;700&family=Roboto:wght@400;500&display=swap" rel="stylesheet">
<style>
  :root {
    --cyan: #0db0e1;
    --cyan-dark: #0796c8;
    --navy: #0b2a6e;
    --navy-deep: #0a2466;
    --brand: #3277b5;
    --text: #7a7a7a;
    --text-dark: #333;
    --line: #d9eef6;
    --white: #ffffff;
  }
  * { box-sizing: border-box; margin: 0; padding: 0; }
  html, body { width: 1200px; height: 3525px; overflow: hidden; }
  body { position: relative; background: var(--white); font-family: "Roboto", Arial, sans-serif; color: var(--text); }
  .abs { position: absolute; }
  .heading { font-family: "Raleway", Arial, sans-serif; font-weight: 600; color: var(--navy); text-transform: uppercase; }
  .heading .accent { color: var(--cyan); }
  .rule { position: absolute; height: 3px; background: var(--cyan); }
  .btn { position: absolute; display: flex; align-items: center; justify-content: center; border-radius: 30px; background: var(--cyan); color: var(--white); font-family: "Raleway", Arial, sans-serif; font-weight: 600; text-transform: uppercase; }

  /* header */
  .site-header { position: absolute; left: 0; top: 0; width: 1200px; height: 132px; background: var(--white); }
  .brand-name { position: absolute; left: 112px; top: 42px; font-family: "Raleway", Arial, sans-serif; font-weight: 700; font-size: 44px; color: var(--navy); letter-spacing: 1px; line-height: 1; }
  .brand-tag { position: absolute; left: 113px; top: 93px; font-family: "Raleway", Arial, sans-serif; font-weight: 600; font-size: 11px; color: var(--navy); }
  .main-nav a { position: absolute; top: 61px; font-family: "Raleway", Arial, sans-serif; font-weight: 600; font-size: 14px; color: #222; text-decoration: none; }
  .main-nav a.active { color: var(--cyan); }

  /* hero */
  .hero-photo { position: absolute; left: 0; top: 132px; width: 1200px; height: 720px; background: linear-gradient(100deg, #b8c2cc 0%, #6e8296 25%, #3c5670 50%, #344b63 75%, #54687c 100%); }
  .hero-curve { position: absolute; left: 0; top: 132px; }
  .hero-title { left: 679px; top: 238px; font-family: "Raleway", Arial, sans-serif; font-weight: 600; font-size: 78px; color: var(--white); line-height: 1; }
  .hero-sub { left: 680px; top: 328px; font-family: "Raleway", Arial, sans-serif; font-weight: 500; font-size: 22px; color: var(--white); text-transform: uppercase; }

  /* services */
  .service-card { position: absolute; top: 1015px; width: 308px; height: 374px; border: 1px solid var(--line); background: var(--white); box-shadow: 0 2px 8px rgba(13,176,225,.08); text-align: center; }
  .service-card svg { position: absolute; left: 98px; top: 34px; }
  .service-card h3 { position: absolute; left: 0; top: 166px; width: 100%; font-family: "Raleway", Arial, sans-serif; font-weight: 600; font-size: 20px; color: var(--navy); }
  .service-card p { position: absolute; left: 22px; top: 204px; width: 262px; font-size: 14px; line-height: 26px; }
  .service-card .btn { left: 86px; top: 300px; width: 136px; height: 46px; font-size: 14px; }

  /* welcome */
  .welcome-text { left: 112px; top: 1592px; width: 443px; font-size: 13.6px; line-height: 25.8px; text-align: justify; }
  .welcome-art { position: absolute; left: 590px; top: 1480px; width: 610px; height: 430px; background: radial-gradient(ellipse at 60% 45%, #c9d8f4 0%, #e6edfb 45%, #ffffff 75%); }

  /* vaccination band */
  .vaccine-band { position: absolute; left: 0; top: 1970px; width: 1200px; height: 525px; background: linear-gradient(110deg, #0ad7f4 0%, #1cbde9 40%, #06b2e3 70%, #02a9dc 100%); }
  .vaccine-title { left: 702px; top: 2100px; font-family: "Raleway", Arial, sans-serif; font-weight: 600; font-size: 34px; color: var(--white); }
  .vaccine-text { left: 702px; top: 2161px; width: 430px; font-size: 13.6px; line-height: 27px; color: var(--white); }

  /* blog */
  .blog-post { position: absolute; top: 2642px; width: 313px; }
  .blog-post .photo { width: 313px; height: 233px; }
  .blog-post .date { margin-top: 18px; font-family: "Raleway", Arial, sans-serif; font-weight: 600; font-size: 20px; color: var(--cyan); }
  .blog-post h4 { margin-top: 12px; font-family: "Raleway", Arial, sans-serif; font-weight: 600; font-size: 18px; color: #2a2a2a; }
  .blog-post p { margin-top: 10px; font-size: 13.6px; line-height: 26px; }

  /* footer */
  .site-footer { position: absolute; left: 0; top: 3100px; width: 1200px; height: 425px; background: var(--navy-deep); color: var(--white); }
  .footer-brand { position: absolute; left: 142px; top: 190px; font-family: "Raleway", Arial, sans-serif; font-weight: 700; font-size: 74px; color: var(--white); line-height: 1; }
  .footer-tag { position: absolute; left: 143px; top: 262px; font-family: "Raleway", Arial, sans-serif; font-weight: 500; font-size: 17px; color: var(--white); }
  .footer-dot { position: absolute; left: 236px; top: 108px; width: 100px; height: 60px; border-radius: 50%; background: var(--cyan); }
  .footer-h { position: absolute; font-family: "Raleway", Arial, sans-serif; font-weight: 600; font-size: 22px; text-transform: uppercase; }
  .contact-item { position: absolute; left: 525px; font-size: 15px; line-height: 23px; letter-spacing: .5px; }
  .contact-icon { position: absolute; left: 485px; }
  .news-text { position: absolute; left: 763px; top: 108px; width: 330px; font-size: 13.6px; line-height: 25px; }
  .news-input { position: absolute; left: 762px; top: 188px; width: 326px; height: 41px; background: var(--white); border: 1px solid #ccc; color: #666; font-size: 15px; padding: 11px 19px; }
  .copyright { position: absolute; left: 0; top: 378px; width: 1200px; text-align: center; font-size: 14px; }
</style>
</head>
<body>

<header class="site-header">
  <div class="brand-name">NUBRIX</div>
  <div class="brand-tag">Modern Digital Software Solutions</div>
  <nav class="main-nav">
    <a class="active" style="left:578px">HOME</a>
    <a style="left:669px">ABOUT US</a>
    <a style="left:789px">SERVICES</a>
    <a style="left:907px">NEWS</a>
    <a style="left:998px">CONTACT US</a>
  </nav>
</header>

<section class="hero">
  <div class="hero-photo" role="img" aria-label="Photo of a doctor's hand touching a glowing digital medical interface"></div>
  <svg class="hero-curve" width="1200" height="720" viewBox="0 0 1200 720">
    <path d="M0 648 C150 720 330 730 520 650 L1200 282 L1200 720 L0 720 Z" fill="#ffffff"/>
    <path d="M0 648 C150 720 330 730 520 650 L1200 282" fill="none" stroke="#0db0e1" stroke-width="6"/>
  </svg>
  <div class="abs hero-title">NUBRIX</div>
  <div class="abs hero-sub">Modern Digital Software Solutions</div>
  <div class="btn" style="left:679px;top:383px;width:178px;height:56px;font-size:17px">Read More</div>
</section>

<section class="services">
  <h2 class="abs heading" style="left:0;top:906px;width:1200px;text-align:center;font-size:38px">Our <span class="accent">Services</span></h2>
  <div class="rule" style="left:582px;top:963px;width:36px"></div>

  <article class="service-card" style="left:112px">
    <svg width="110" height="100" viewBox="0 0 110 100" fill="none" stroke="#3277b5" stroke-width="3">
      <rect x="4" y="4" width="32" height="24"/><rect x="74" y="4" width="32" height="24"/>
      <rect x="4" y="66" width="32" height="24"/><rect x="74" y="66" width="32" height="24"/>
      <path d="M36 16h38M20 28v38M90 28v38M36 78h38"/>
      <path d="M40 52a8 8 0 0 1 10-10a10 10 0 0 1 18 4a7 7 0 0 1 0 14h-26a6 6 0 0 1-2-8z" fill="#9fd3f2"/>
    </svg>
    <h3>SERVICES 01</h3>
    <p>Sed ut perspiciatis unde omnis iste nat us error sit voluptatem accusantium laudantium totam aperia</p>
    <div class="btn">Read More</div>
  </article>

  <article class="service-card" style="left:446px">
    <svg width="110" height="110" viewBox="0 0 110 110" fill="none" stroke="#3277b5" stroke-width="3">
      <rect x="18" y="4" width="74" height="26" fill="#9fd3f2"/><rect x="18" y="30" width="74" height="26" fill="#9fd3f2"/><rect x="18" y="56" width="74" height="26" fill="#9fd3f2"/>
      <circle cx="76" cy="17" r="5"/><circle cx="76" cy="43" r="5"/><circle cx="76" cy="69" r="5"/>
      <path d="M28 17h8M42 17h8M28 43h8M42 43h8M28 69h8M42 69h8M55 82v16M20 102h28M62 102h28"/>
      <circle cx="55" cy="102" r="7"/>
    </svg>
    <h3>SERVICES 02</h3>
    <p>Sed ut perspiciatis unde omnis iste nat us error sit voluptatem accusantium laudantium totam aperia</p>
    <div class="btn">Read More</div>
  </article>

  <article class="service-card" style="left:780px">
    <svg width="130" height="104" viewBox="0 0 130 104" fill="none" stroke="#3277b5" stroke-width="3">
      <circle cx="50" cy="50" r="44"/><ellipse cx="50" cy="50" rx="20" ry="44"/>
      <path d="M6 50h88M12 28h76M12 72h76M50 6v88"/>
      <path d="M58 90a12 12 0 0 1 8-22a18 18 0 0 1 34-4a14 14 0 0 1 22 14a12 12 0 0 1-4 22h-56a10 10 0 0 1-4-10z" fill="#9fd3f2"/>
    </svg>
    <h3>SERVICES 03</h3>
    <p>Sed ut perspiciatis unde omnis iste nat us error sit voluptatem accusantium laudantium totam aperia</p>
    <div class="btn">Read More</div>
  </article>
</section>

<section class="welcome">
  <div class="welcome-art" role="img" aria-label="Isometric illustration of a cloud with servers connected to computers"></div>
  <h2 class="abs heading" style="left:112px;top:1514px;font-size:34px">Welcome to <span class="accent">NUBRIX</span></h2>
  <div class="rule" style="left:112px;top:1567px;width:58px;background:var(--navy)"></div>
  <p class="abs welcome-text">Sed ut perspiciatis unde omnis iste natus error sit voluptatem accus antium doloremque laudantium, totam rem aperiam, eaque ipsa quae ab illo inventore veritatis et quasi architecto beatae vitae dicta sunt explicabo. Nemo enim ipsam voluptatem quia voluptas sit aspernatur aut odit aut fugit, sed quia consequuntur magni dolores eos qui ratione voluptatem sequi nesciunt. Neque porro quisquam est, qui dolorem ipsum audantium, totam remquia dolor sit amet, sed ut perspiciatis unde omnis iste natus error sit voluptatem accus antium doloremque laudantium, totam rem quasi architecto beatae vitae dicta sunt explicabo</p>
  <div class="btn" style="left:112px;top:1854px;width:156px;height:52px;font-size:15px">Read More</div>
</section>

<section class="vaccine-band" role="img" aria-label="Cyan-toned photo of a patient receiving a vaccine injection in the arm"></section>
<h2 class="abs vaccine-title">VACCINATION SERVICES</h2>
<p class="abs vaccine-text">Sed ut perspiciatis unde omnis iste natus error sit voluptatem accusa ntium doloremque laudantium, totam rem aperiam, eaque ipsa quae architecto beatae vitae dicta sunt explicabo.</p>
<div class="btn" style="left:702px;top:2269px;width:162px;height:54px;font-size:15px;background:var(--navy)">Read More</div>

<section class="blog">
  <h2 class="abs heading" style="left:0;top:2550px;width:1200px;text-align:center;font-size:38px">Latest <span class="accent">Blog</span></h2>
  <div class="rule" style="left:582px;top:2603px;width:36px"></div>

  <article class="blog-post" style="left:112px">
    <div class="photo" role="img" aria-label="Photo of a person sketching a network diagram beside a laptop" style="background:linear-gradient(135deg,#6b5a45,#c9bda8 55%,#e8e2d6)"></div>
    <div class="date">24 MAR 2021</div>
    <h4>Nemo enim ipsam voluptatem</h4>
    <p>Sed ut perspiciatis unde omnis iste natus error sit voluptatem accusantium doloremque lauda ntium, totam rem aperiam</p>
  </article>
  <article class="blog-post" style="left:444px">
    <div class="photo" role="img" aria-label="Photo of two engineers with a laptop in a server room" style="background:linear-gradient(135deg,#2c3035,#6c737a 50%,#1e2226)"></div>
    <div class="date">24 MAR 2021</div>
    <h4>Nemo enim ipsam voluptatem</h4>
    <p>Sed ut perspiciatis unde omnis iste natus error sit voluptatem accusantium doloremque lauda ntium, totam rem aperiam</p>
  </article>
  <article class="blog-post" style="left:776px">
    <div class="photo" role="img" aria-label="Photo of hands typing on a laptop with blue binary code overlay" style="background:linear-gradient(135deg,#8c6a6a,#3a4f86 50%,#1d2e6a)"></div>
    <div class="date">24 MAR 2021</div>
    <h4>Nemo enim ipsam voluptatem</h4>
    <p>Sed ut perspiciatis unde omnis iste natus error sit voluptatem accusantium doloremque lauda ntium, totam rem aperiam</p>
  </article>
</section>

<footer class="site-footer">
  <div class="footer-dot"></div>
  <div class="footer-brand">NUBRIX</div>
  <div class="footer-tag">Modern Digital Software Solutions</div>

  <div class="footer-h" style="left:484px;top:80px">Contact Us</div>
  <svg class="contact-icon" style="top:130px" width="20" height="24" viewBox="0 0 20 24" fill="none" stroke="#fff" stroke-width="1.6"><path d="M10 22s7-7.5 7-12.5a7 7 0 0 0-14 0C3 14.5 10 22 10 22z"/><circle cx="10" cy="9.5" r="2.6"/></svg>
  <div class="contact-item" style="top:128px">Address<br>#215 Lorem Ipsum<br>Dummy Text Lorem</div>
  <svg class="contact-icon" style="top:216px" width="22" height="22" viewBox="0 0 22 22" fill="none" stroke="#fff" stroke-width="1.6"><path d="M5 2l4 4-2.5 2.5a12 12 0 0 0 7 7L16 13l4 4-3 3C9 19 3 13 2 5z"/></svg>
  <div class="contact-item" style="top:218px">Phone :<br>000-121-1231</div>
  <svg class="contact-icon" style="top:284px" width="22" height="16" viewBox="0 0 22 16" fill="none" stroke="#fff" stroke-width="1.6"><rect x="1" y="1" width="20" height="14"/><path d="M1 1l10 8 10-8"/></svg>
  <div class="contact-item" style="top:280px">Email :<br>info@company.com</div>

  <div class="footer-h" style="left:763px;top:76px">Newsletter</div>
  <p class="news-text">Sed ut perspiciatis unde omnis iste natus error sit voluptatem accusantium doloremque</p>
  <div class="news-input">Enter Email</div>
  <div class="btn" style="left:760px;top:247px;width:145px;height:46px;font-size:15px">Subscribe</div>

  <div class="copyright">© Copyright 2021.All Rights Reserved</div>
</footer>

</body>
</html>
```